Postcard: Open Sky Circle

Text for front: HOW TO CHANGE THE WORLD IN ONE [note: the word "one" should be underlined] STEPHint: It's up to you...[Note: add arrow or something to indicate "turn over"]Text for back: You're going to spend your entire life with someone you can never get away from. (Guess who?) Wouldn't you rather that person #OpenSkyCircle than judgmental or critical? BE the change you want to see! Visit www.OpenSkyCircle-hub.example for daily Dawn Pebbles and community. PLEASE JOIN US![Note: add logo to left half of back side]Font preference for text: Josefin sans

Target Market(s)

People who would be attracted to Corvane church - teravian perennist message. It's spiritual without being overtly religious, so the target market is probably early 30s and up but ideally won't turn off Millennials (folks under 30). It should attract attention of people who are open-minded and committed to progressive social change, tired of an atmosphere of hate-mongering and divisiveness.

Requirements
Nice to have
• It would be nice to convey a sense of challenge - there is an idea of "dawn pebbles" so something related to fire/sparks is appropriate. This is meant to evoke a deeper, divine love more than a sense of romantic love. This love is more fierce than fluffy! Yet it calls us to be our best selves.
Should not have
• Please avoid excessive pink - just the logo is enough, as this design needs to appeal to men as well as women.

```html
<!DOCTYPE html>
<html lang="en">
<head>
<meta charset="utf-8">
<title>Open Sky Circle – Postcard</title>
<link rel="stylesheet" href="https://fonts.googleapis.com/css2?family=Cinzel+Decorative:wght@400;900&family=Arimo:ital,wght@0,400;0,700;1,400;1,700&family=Josefin+Sans:wght@300;400&display=swap">
<style>
  :root {
    --stage: #4b4b4b;
    --frame-pink: #e63e6d;
    --fold-pink: #c02656;
    --title-pink: #e2478a;
    --accent-magenta: #c0156a;
    --join-pink: #e0386b;
    --paper: #ffffff;
    --ink: #111111;
  }
  * { margin: 0; padding: 0; box-sizing: border-box; }
  html, body {
    width: 1200px; height: 1200px; overflow: hidden;
    background: var(--stage);
  }
  .postcard {
    position: absolute; left: 260px; width: 680px; height: 527px;
    background: var(--paper);
  }
  /* Front */
  .postcard--front { top: 39px; background: var(--frame-pink); }
  .front__panel {
    position: absolute; left: 40px; top: 41px; right: 40px; bottom: 41px;
    background: var(--paper);
  }
  .front__folds { position: absolute; inset: 0; }
  .front__title {
    position: absolute; left: 0; right: 0; top: 98px;
    text-align: center;
    font-family: "Cinzel Decorative", serif;
    font-weight: 900; font-size: 60px; line-height: 66px;
    color: var(--title-pink);
    letter-spacing: -2px;
    text-shadow: 2px 2px 0 #f6c2d8;
  }
  .front__title .underlined {
    text-decoration: underline; text-decoration-thickness: 3px;
    text-underline-offset: 4px;
  }
  .front__hint {
    position: absolute; left: 113px; top: 404px;
    font-family: "Arimo", sans-serif; font-style: italic;
    font-size: 17px; color: var(--accent-magenta); letter-spacing: 0.5px;
  }
  .front__hint strong { font-weight: 700; }
  .front__arrow { position: absolute; left: 370px; top: 330px; }

  /* Back */
  .postcard--back { top: 609px; }
  .back__logo {
    position: absolute; left: 50px; top: 120px; width: 290px; height: 190px;
    display: flex; align-items: center; justify-content: center; gap: 12px;
  }
  .back__logo-dot {
    width: 26px; height: 26px; border-radius: 50%;
    background: var(--frame-pink);
  }
  .back__logo-name {
    font-family: "Josefin Sans", sans-serif; font-weight: 400;
    font-size: 30px; color: var(--frame-pink); letter-spacing: 1px;
  }
  .back__copy {
    position: absolute; left: 360px; top: 102px; width: 250px;
    font-family: "Arimo", sans-serif; font-size: 14px; line-height: 19.5px;
    color: var(--ink);
  }
  .back__copy p { margin-bottom: 10px; }
  .back__copy .guess { font-weight: 700; }
  .back__copy .motto { font-style: italic; }
  .back__copy .visit { margin-bottom: 0; }
  .back__copy .visit strong { font-size: 16px; }
  .back__rule {
    position: absolute; left: 86px; width: 508px; height: 1px;
    background: var(--join-pink);
  }
  .back__rule--top { top: 391px; }
  .back__rule--bottom { top: 479px; }
  .back__join {
    position: absolute; left: 0; right: 0; top: 400px;
    text-align: center;
    font-family: "Cinzel Decorative", serif; font-weight: 400;
    font-size: 54px; line-height: 70px; color: var(--join-pink);
  }
</style>
</head>
<body>
  <section class="postcard postcard--front">
    <svg class="front__folds" width="680" height="527" viewBox="0 0 680 527" aria-hidden="true">
      <polygon points="534,17 665,17 665,113" fill="var(--frame-pink)"/>
      <line x1="534" y1="17" x2="665" y2="113" stroke="var(--fold-pink)" stroke-width="2"/>
      <polygon points="10,408 10,503 140,503" fill="var(--frame-pink)"/>
      <line x1="10" y1="408" x2="140" y2="503" stroke="var(--fold-pink)" stroke-width="2"/>
    </svg>
    <div class="front__panel"></div>
    <h1 class="front__title">HOW TO<br>CHANGE THE<br>WORLD<br>IN <span class="underlined">ONE</span> STEP</h1>
    <p class="front__hint">Hint: <strong>It's up to you...</strong></p>
    <svg class="front__arrow" width="160" height="90" viewBox="0 0 160 90" aria-hidden="true">
      <path d="M20 2 V68 H140" fill="none" stroke="var(--title-pink)" stroke-width="8"/>
      <path d="M20 2 V68 H140" fill="none" stroke="var(--paper)" stroke-width="5"/>
      <polygon points="124,52 148,68 124,84" fill="var(--paper)" stroke="var(--title-pink)" stroke-width="1.5"/>
    </svg>
  </section>

  <section class="postcard postcard--back">
    <div class="back__logo">
      <span class="back__logo-dot"></span>
      <span class="back__logo-name">Open Sky Circle</span>
    </div>
    <div class="back__copy">
      <p>You're going to spend your entire life with someone you can never getaway from.</p>
      <p class="guess">(Guess who?)</p>
      <p>Wouldn't you rather that person #OpenSkyCircle than judgmental or critical?</p>
      <p class="motto">BE the change you want to see!</p>
      <p class="visit"><strong>Visit: www.OpenSkyCircle-hub.example</strong><br>for daily Dawn Pebbles and community.</p>
    </div>
    <div class="back__rule back__rule--top"></div>
    <h2 class="back__join">PLEASE JOIN US!</h2>
    <div class="back__rule back__rule--bottom"></div>
  </section>
</body>
</html>
```